website in progress for new building development

Hi,
I have a new real estate development website in making but am running out of time for its completion. It's for a new apartment building for sales. Would it be possible for you to change/alter the site according to my requirements? I could send you all the existing files. The bulk of the website is done.
The images aren't really ready yet but will be within the next days so those will need to be replaced. Currently draft images are the placeholder on the website.

Let me know if you would be interested so we can quickly pick up correspondence.

This is the website so far (using Wordpress):
http://lindmoor.com.au/lindmoor/

Our domain is:
lindmoor.com.au

I am also adding the theme I am using.

Thanks.

Target Market(s)

Potential buyers.

Industry/Entity Type

Real Estate Development

Number of Pages Required

5+ page

Font styles to use
Other font styles liked:
• I used Robot under google fonts for the headlines

Requirements
Must have
• This is the current website
• http://lindmoor.com.au/lindmoor
• I'd like the colour scheme to remain the way it is.
• 1. Header
• I would like the header to have the menu on the right and have the 'Reigster' button similar to this website: (see the header here which shows up once you scroll down in the page) http://zenithbyfalconhouse.com.au/
• Please adjust this feature into our website with the menu items given.
• 2. Logo on Homepage
• Add the lindmoor logo into the top center of the feature image.
• Though permanent images are yet to arrive in the next few days. These are only drafts.
• 3. Footer
• Not sure about the colour scheme here yet.
• Should contain Disclaimer and copyrights.
• 4.Pages:
• a) Home
• b) Building
• c) Interior
• d) Location
• e) Register
• 5. page 'Home'
• When you scroll down in lindmoor.com.au/lindmoor/ you see the three images under the feature image, I would like those being hyperlinked as a 'box' just like this website has them when you scroll down here:
• http://www.velmotide.com.au/
• 6. page 'Register'
• I like the subtle colour scheme for the form used here http://zenithbyfalconhouse.com.au/#enquire-now
• and their 'Submit' button. Maybe adjust it to my website and remove the borders in the fields.
• 7. page 'Building'
• Will have two images of the exterior of the building which should be sliding automatically. (Images will be provided soon. For now I am only attaching draft images.)
• 8. page 'Interior'
• Will also have two images of the interior which should be automatically sliding. (Images will be provided soon. Attaching draft images for now)
Nice to have
• A language selection in the top right corner of each page:
• selection between english, mandarin, cantonese, korean.

```html
<!DOCTYPE html>
<html lang="en">
<head>
<meta charset="utf-8">
<title>Lindmoor – Contemporary Parkside Living</title>
<link href="https://fonts.googleapis.com/css2?family=Roboto:wght@300;400;500;700&display=swap" rel="stylesheet">
<style>
:root{
  --dark:#1c1c1c;
  --darker:#141414;
  --gold:#d6a24a;
  --text:#6a6a6a;
  --light:#ffffff;
  --panel:#262626;
  --form-bg:#ececec;
}
*{margin:0;padding:0;box-sizing:border-box}
html,body{width:687px;height:1200px;overflow:hidden}
body{font-family:'Roboto',sans-serif;background:var(--light);color:var(--text);position:relative}
.site-header{height:70px;background:var(--dark);display:flex;align-items:center;justify-content:space-between;padding:0 26px}
.brand{display:flex;align-items:center;gap:8px;color:var(--gold);font-weight:500;font-size:13px;letter-spacing:2px}
.brand-mark{width:18px;height:18px;background:var(--gold)}
.main-nav{display:flex;align-items:center;gap:14px}
.main-nav a{color:var(--gold);font-size:8px;letter-spacing:.6px;text-decoration:none;text-transform:uppercase}
.main-nav .register-btn{background:var(--gold);color:#fff;padding:7px 13px;font-weight:500}
.hero{position:relative;height:354px;background:linear-gradient(180deg,#1f2f4d 0%,#3b5a85 18%,#7d5a4c 40%,#9b6a52 55%,#4b4a48 78%,#2f2d2c 100%)}
.hero-brand{position:absolute;left:50%;top:22px;transform:translateX(-50%);display:flex;align-items:center;gap:9px;color:var(--light);font-size:18px;font-weight:500;letter-spacing:4px}
.hero-brand .brand-mark{width:22px;height:22px}
.intro{text-align:center;padding:30px 60px 0}
.intro h1{color:var(--gold);font-size:12px;font-weight:500;letter-spacing:3px;margin-bottom:16px}
.intro p{font-size:7px;line-height:1.6;margin-bottom:12px}
.features{display:flex;margin-top:18px}
.feature{width:229px}
.feature-photo{height:195px}
.feature-photo.building{background:linear-gradient(170deg,#dfe6ee 0%,#b8bcc0 30%,#8a6f5e 65%,#4e4a47 100%)}
.feature-photo.interior{background:linear-gradient(170deg,#f1ede6 0%,#d9cfbf 40%,#a99276 75%,#6d5e4e 100%)}
.feature-photo.location{background:linear-gradient(170deg,#e6ecf2 0%,#c9cfd4 35%,#a58f7d 70%,#5a5552 100%)}
.feature-body{height:114px;background:var(--panel);padding:20px 14px;color:#ddd}
.feature.is-active .feature-body{background:var(--gold)}
.feature-body h2{font-size:14px;font-weight:500;color:#fff;margin-bottom:5px}
.feature-body p{font-size:7px;line-height:1.5}
.contact{padding:14px 60px 0}
.contact h2{text-align:center;color:var(--gold);font-size:10px;letter-spacing:3px;font-weight:500;margin-bottom:14px}
.enquiry-form{display:flex;gap:8px;background:var(--form-bg);padding:12px}
.field-col{display:flex;flex-direction:column;gap:7px;width:160px}
.field{height:20px;background:#fff;font-size:7px;color:#999;padding:6px 7px}
.message{flex:1;background:#fff;font-size:7px;color:#999;padding:6px 7px;height:81px}
.send-btn{width:82px;background:var(--gold);color:#fff;font-size:9px;font-weight:500;display:flex;align-items:center;justify-content:center;letter-spacing:1px}
.site-footer{position:absolute;left:0;top:1025px;width:687px;height:147px;background:var(--dark);display:flex;padding:18px 42px;color:#bbb;font-size:7px}
.site-footer h3{color:#fff;font-size:8px;font-weight:500;letter-spacing:1px;margin-bottom:12px}
.footer-col{flex:1}
.info-row{display:flex;gap:8px;align-items:flex-start;margin-bottom:11px;line-height:1.4}
.info-row svg{flex:none}
.quick-links li{list-style:none;margin-bottom:5px}
.socials{display:flex;gap:16px}
.social{text-align:center;color:var(--gold);font-size:7px}
.social-ring{width:34px;height:34px;border:2px solid var(--gold);border-radius:50%;margin:0 auto 5px}
.bottom-bar{position:absolute;left:0;top:1172px;width:687px;height:28px;background:var(--darker);display:flex;align-items:center;justify-content:space-between;padding:0 42px;color:#999;font-size:7px}
</style>
</head>
<body>
<header class="site-header">
  <div class="brand"><span class="brand-mark"></span>LINDMOOR</div>
  <nav class="main-nav">
    <a href="#">Home</a><a href="#">Building</a><a href="#">Interior</a><a href="#">Location</a>
    <a href="#" class="register-btn">Register Now</a>
  </nav>
</header>

<section class="hero" role="img" aria-label="Dusk view of the red-brick apartment building across a tree-lined street">
  <div class="hero-brand"><span class="brand-mark"></span>LINDMOOR</div>
</section>

<section class="intro">
  <h1>CONTEMPORARY PARKSIDE LIVING</h1>
  <p>Located on a quiet suburban street, Lindmoor is a thriving and contemporary boutique development that opens up to the peace and tranquillity of the great outdoors.</p>
  <p>Artfully conceived and expertly detailed, Lindmoor is a distinctive boutique collection of only 31 apartments, perfectly located between the beach and the convenience of local shops. A landscaped garden offers a peaceful setting, and every living space flows naturally to generous balconies.</p>
</section>

<section class="features">
  <a class="feature">
    <div class="feature-photo building" role="img" aria-label="Exterior of the apartment building"></div>
    <div class="feature-body"><h2>BUILDING</h2><p>A little text here</p></div>
  </a>
  <a class="feature is-active">
    <div class="feature-photo interior" role="img" aria-label="Bright open-plan living room interior"></div>
    <div class="feature-body"><h2>INTERIOR</h2><p>Superbly finished and perfectly appointed, each apartment is the result of a refined yet practical architectural vision.</p></div>
  </a>
  <a class="feature">
    <div class="feature-photo location" role="img" aria-label="Corner view of the building and its street location"></div>
    <div class="feature-body"><h2>LOCATION</h2><p>A little text here</p></div>
  </a>
</section>

<section class="contact">
  <h2>CONTACT US</h2>
  <form class="enquiry-form">
    <div class="field-col">
      <div class="field">First &amp; Last Name*</div>
      <div class="field">Phone Number</div>
      <div class="field">Email Address*</div>
    </div>
    <div class="message">Your Message*</div>
    <div class="send-btn">SEND</div>
  </form>
</section>

<footer class="site-footer">
  <div class="footer-col">
    <h3>CONTACT INFO</h3>
    <div class="info-row"><svg width="10" height="12" viewBox="0 0 10 12"><path d="M5 0a4 4 0 0 0-4 4c0 3 4 8 4 8s4-5 4-8a4 4 0 0 0-4-4z" fill="none" stroke="#bbb"/></svg><span>14 Wattle Lane, Brookvale<br>NSW</span></div>
    <div class="info-row"><svg width="10" height="10" viewBox="0 0 10 10"><circle cx="5" cy="5" r="4.5" fill="none" stroke="#bbb"/></svg><span>0400 000 000</span></div>
    <div class="info-row"><svg width="10" height="10" viewBox="0 0 10 10"><circle cx="5" cy="5" r="4.5" fill="none" stroke="#bbb"/></svg><span>info@lindmoor.com.au</span></div>
  </div>
  <div class="footer-col">
    <h3>QUICK LINKS</h3>
    <ul class="quick-links"><li>› Home</li><li>› Building</li><li>› Interior</li><li>› Location</li><li>› Register</li><li>› Credits</li></ul>
  </div>
  <div class="footer-col">
    <h3>CONNECT WITH US</h3>
    <div class="socials">
      <div class="social"><div class="social-ring"></div>Community</div>
      <div class="social"><div class="social-ring"></div>Updates</div>
      <div class="social"><div class="social-ring"></div>Network</div>
    </div>
  </div>
</footer>
<div class="bottom-bar"><span>© 2015 Lindmoor. All Rights Reserved.</span><span>Privacy Policy | Terms of Use</span></div>
</body>
</html>
```